Quote Cards With TK May 2025 for Instagram

I would like to put these quotes over one of the pictures attached; Instagram (new size: 4:5 (1080 x 1350 pixels) One Quote per picture, and I want the quote to be bold or easy to read as well. I provided a few reference graphics that I really like as examples below. In very small letters at the bottom add @TKBarlowOnline

All of the pictures are attached; you can pick any photo and add one quote to it; but no stock photography

```html
<!DOCTYPE html>
<html lang="en">
<head>
<meta charset="utf-8">
<title>Quote Cards with TK</title>
<link href="https://fonts.googleapis.com/css2?family=Oswald:wght@300;400&display=swap" rel="stylesheet">
<style>
  :root {
    --bg: #000000;
    --ink: #ffffff;
    --tint: rgba(88, 62, 96, 0.62);
    --tint-soft: rgba(88, 62, 96, 0.18);
  }
  * { margin: 0; padding: 0; box-sizing: border-box; }
  html, body { width: 1200px; height: 594px; overflow: hidden; background: var(--bg); }
  .board {
    position: relative;
    width: 1200px; height: 594px;
    display: grid;
    grid-template-columns: repeat(5, 224px);
    grid-template-rows: repeat(2, 280px);
    column-gap: 9.5px; row-gap: 11px;
    padding: 12px 0 0 21.5px;
  }
  .card { position: relative; overflow: hidden; }
  .card__photo { position: absolute; inset: 0; }
  .card__panel {
    position: absolute; top: 0; bottom: 0; left: 44%; right: 0;
    background: linear-gradient(90deg, var(--tint-soft), var(--tint) 18%, var(--tint));
  }
  .card--flip .card__panel { left: 0; right: 0; background: linear-gradient(90deg, rgba(150,50,150,.55), rgba(150,50,150,.35) 55%, rgba(120,40,140,.1)); }
  .card__copy {
    position: absolute; top: var(--top); left: 42%; right: 0;
    display: flex; flex-direction: column; align-items: center;
    color: var(--ink); text-align: center;
    font-family: "Oswald", sans-serif;
  }
  .card--flip .card__copy { left: 0; right: 46%; }
  .card__quote { font-weight: 300; font-size: 15.5px; line-height: 21.3px; letter-spacing: -0.2px; }
  .card__handle { margin-top: 26px; font-weight: 400; font-size: 8.2px; letter-spacing: 1.4px; text-transform: uppercase; }
</style>
</head>
<body>
<main class="board">
  <article class="card card--flip" style="--top:70px">
    <div class="card__photo" role="img" aria-label="TK in a pink gown on a stage" style="background:linear-gradient(110deg,#8a3a86,#b4459a 55%,#d05ab0)"></div>
    <div class="card__panel"></div>
    <div class="card__copy"><p class="card__quote">Tired.Moody.<br>Stubborn Belly Fat.<br>Your hormones are<br>screaming for help!<br>Let’s fix that.</p><p class="card__handle">@TKBarlowOnline</p></div>
  </article>
  <article class="card" style="--top:53px">
    <div class="card__photo" role="img" aria-label="TK courtside holding a basketball" style="background:linear-gradient(120deg,#4a4658,#7a5a78 40%,#3a3040)"></div>
    <div class="card__panel"></div>
    <div class="card__copy"><p class="card__quote">What worked in<br>your 30s won’t<br>work now.<br>Here’s what<br>actually does. Drop<br>30 Pounds in<br>3 Months.</p><p class="card__handle">@TKBarlowOnline</p></div>
  </article>
  <article class="card" style="--top:53px">
    <div class="card__photo" role="img" aria-label="TK in a black outfit outdoors" style="background:linear-gradient(120deg,#8aa0b8,#2e2a30 35%,#5a6a48 70%,#3a3838)"></div>
    <div class="card__panel"></div>
    <div class="card__copy"><p class="card__quote">This is the secret<br>women over 40<br>are using to<br>get snatched;<br>without starving.<br>Comment SKINNY<br>to get the exact plan.</p><p class="card__handle">@TKBarlowOnline</p></div>
  </article>
  <article class="card" style="--top:65px">
    <div class="card__photo" role="img" aria-label="TK posing in a striped sheer top" style="background:linear-gradient(120deg,#d8d2d4,#3a3236 40%,#7a7070)"></div>
    <div class="card__panel"></div>
    <div class="card__copy"><p class="card__quote">This 90-day plan<br>helped women<br>over 40 slim down,<br>get a tiny waist<br>and feel sexy again.<br>You’re next.</p><p class="card__handle">@TKBarlowOnline</p></div>
  </article>
  <article class="card" style="--top:58px">
    <div class="card__photo" role="img" aria-label="TK in a black outfit with hills behind" style="background:linear-gradient(120deg,#b8c8d8,#2a2628 40%,#6a7050 75%,#8a8078)"></div>
    <div class="card__panel"></div>
    <div class="card__copy"><p class="card__quote">You’re doing all the<br>“right” things,<br>but your belly<br>won’t go down?<br>Here’s what<br>you haven’t tried.</p><p class="card__handle">@TKBarlowOnline</p></div>
  </article>
  <article class="card" style="--top:58px">
    <div class="card__photo" role="img" aria-label="TK standing by a window at night" style="background:linear-gradient(120deg,#2a3a5a,#1e1a22 40%,#6a5446)"></div>
    <div class="card__panel"></div>
    <div class="card__copy"><p class="card__quote">Bloating. Muffin top.<br>Puffy waistline.<br>Your body’s<br>screaming<br>for a different<br>kind of fix. Here it is</p><p class="card__handle">@TKBarlowOnline</p></div>
  </article>
  <article class="card" style="--top:58px">
    <div class="card__photo" role="img" aria-label="TK portrait in a striped sheer top" style="background:linear-gradient(120deg,#6a4a4a,#2a2224 45%,#8a7068)"></div>
    <div class="card__panel"></div>
    <div class="card__copy"><p class="card__quote">Flat tummy in<br>your 40s? It’s still<br>possible! Comment<br>BYE BELLY to get the<br>10 secrets to a<br>flatter tummy</p><p class="card__handle">@TKBarlowOnline</p></div>
  </article>
  <article class="card" style="--top:46px">
    <div class="card__photo" role="img" aria-label="TK in a white cropped sweater" style="background:linear-gradient(120deg,#9a9698,#e8e4e4 30%,#2a2628 60%,#8a8486)"></div>
    <div class="card__panel"></div>
    <div class="card__copy"><p class="card__quote">The<br>stubborn belly fat<br>after 40?<br>It’s not about calories;<br>it’s about your<br>hormones.<br>Here is the fix!</p><p class="card__handle">@TKBarlowOnline</p></div>
  </article>
  <article class="card" style="--top:46px">
    <div class="card__photo" role="img" aria-label="TK from behind in an open-back top" style="background:linear-gradient(120deg,#5a5a66,#1e1c20 40%,#4a4650)"></div>
    <div class="card__panel"></div>
    <div class="card__copy"><p class="card__quote">Your belly isn’t fat . . .<br>it’s hormonal.<br>And here’s<br>how to fix it.<br>Comment HORMONES<br>if nothing is<br>working.</p><p class="card__handle">@TKBarlowOnline</p></div>
  </article>
  <article class="card" style="--top:39px">
    <div class="card__photo" role="img" aria-label="TK in pink among sunflowers" style="background:linear-gradient(120deg,#a8b8c8,#c89a3a 30%,#b07090 50%,#8a6a40)"></div>
    <div class="card__panel"></div>
    <div class="card__copy"><p class="card__quote">That stubborn<br>weight?<br>It’s not your fault.<br>Your hormones are<br>to blame and<br>you’re not alone;<br>But there is a fix.</p><p class="card__handle">@TKBarlowOnline</p></div>
  </article>
</main>
</body>
</html>
```